Boutique custom software development company needs new business card

Our nearly 20 year old custom software development company would like to better include the fact that we are now providing Bitcoin services. These new services are B2B include education (how to acquire and securely hold Bitcoin) and integrating Bitcoin payments into existing ecommerce sites or other existing systems. Please keep the card clean and simple. Attached is our current design and some other files. vexalon.example

Target Market(s)

businesses owners interested in long term relationship

Industry/Entity Type

Custom software development and Bitcoin

Contact Information for Business Card

Marcus Ellwood, marcus@vexalon.example, vexalon.example, (888) 555-VEXAL

Font styles to use
Other font styles liked:
• monospace

Requirements
Must have
• double-sided
Nice to have
• clean and simple
Should not have
• physical address

```html
<!DOCTYPE html>
<html lang="en">
<head>
<meta charset="utf-8">
<title>Vexalon Business Card</title>
<link href="https://fonts.googleapis.com/css2?family=Montserrat:wght@400;500;700&family=Open+Sans:wght@400;600&display=swap" rel="stylesheet">
<style>
  :root {
    --bg: #e9eaec;
    --white: #ffffff;
    --paper: #f7f7f7;
    --blue: #0870bd;
    --orange: #f5821f;
    --ink: #2b2b2b;
  }
  * { margin: 0; padding: 0; box-sizing: border-box; }
  html, body { width: 1200px; height: 1200px; overflow: hidden; background: var(--bg); }
  body { position: relative; font-family: "Montserrat", sans-serif; }

  .card {
    position: absolute;
    left: 180px;
    width: 840px;
    height: 480px;
    border-radius: 30px;
    overflow: hidden;
    box-shadow: 0 10px 30px rgba(0,0,0,0.18);
  }

  /* Front */
  .card-front { top: 90px; background: linear-gradient(180deg, var(--white), var(--paper)); }
  .brand-mark {
    position: absolute; top: 80px; right: 90px;
    display: flex; align-items: center; gap: 16px;
  }
  .brand-square { width: 48px; height: 48px; background: var(--blue); }
  .brand-name { font-weight: 700; font-size: 42px; color: var(--blue); letter-spacing: 2px; line-height: 1; }
  .services-note {
    position: absolute; top: 144px; right: 90px;
    font-weight: 500; font-size: 15px; color: var(--orange);
    letter-spacing: 1px; text-transform: uppercase;
  }

  .person { position: absolute; left: 90px; top: 225px; }
  .person-name { font-weight: 700; font-size: 40px; color: var(--orange); letter-spacing: 1px; line-height: 1; text-transform: uppercase; }
  .person-title { font-weight: 500; font-size: 17px; color: var(--ink); letter-spacing: 1px; margin-top: 6px; text-transform: uppercase; }

  .contacts { position: absolute; left: 90px; top: 318px; list-style: none; }
  .contacts li { display: flex; align-items: center; gap: 14px; font-size: 23px; color: var(--ink); height: 38px; }
  .contacts svg { width: 24px; height: 24px; fill: var(--orange); flex: none; }

  .band { position: absolute; bottom: 0; height: 22px; }
  .band-orange { left: 0; width: 520px; background: var(--orange); }
  .band-blue { left: 530px; right: 0; background: var(--blue); }

  /* Back */
  .card-back {
    top: 630px; background: var(--blue);
    display: flex; flex-direction: column; align-items: center; justify-content: center;
    text-align: center;
  }
  .back-name { font-weight: 700; font-size: 104px; color: var(--white); letter-spacing: 4px; line-height: 1; }
  .tagline { font-family: "Open Sans", sans-serif; font-size: 34px; color: var(--white); margin-top: 16px; line-height: 1.2; }
  .services {
    margin-top: 22px; display: flex; align-items: center; gap: 14px;
    font-family: "Open Sans", sans-serif; font-weight: 600; font-size: 22px; color: var(--white);
    letter-spacing: 1px;
  }
  .services-dot { width: 12px; height: 12px; border-radius: 50%; background: var(--orange); flex: none; }
</style>
</head>
<body>
  <section class="card card-front">
    <div class="brand-mark">
      <div class="brand-square"></div>
      <span class="brand-name">VEXALON</span>
    </div>
    <p class="services-note">Custom software &amp; Bitcoin services</p>
    <div class="person">
      <p class="person-name">Marcus Ellwood</p>
      <p class="person-title">Founding Partner</p>
    </div>
    <ul class="contacts">
      <li>
        <svg viewBox="0 0 24 24" aria-hidden="true"><path d="M6.6 10.8c1.4 2.8 3.8 5.1 6.6 6.6l2.2-2.2c.3-.3.7-.4 1-.2 1.1.4 2.3.6 3.6.6.6 0 1 .4 1 1V20c0 .6-.4 1-1 1C10.6 21 3 13.4 3 4c0-.6.4-1 1-1h3.5c.6 0 1 .4 1 1 0 1.3.2 2.5.6 3.6.1.3 0 .7-.2 1z"/></svg>
        (888) 555-VEXAL
      </li>
      <li>
        <svg viewBox="0 0 24 24" aria-hidden="true"><path d="M2 5h20v14H2z M3.5 6.5l8.5 6 8.5-6" fill="none" stroke="#f5821f" stroke-width="2"/></svg>
        marcus@vexalon.example
      </li>
      <li>
        <svg viewBox="0 0 24 24" aria-hidden="true"><g fill="none" stroke="#f5821f" stroke-width="1.8"><circle cx="12" cy="12" r="9.5"/><ellipse cx="12" cy="12" rx="4" ry="9.5"/><path d="M2.5 12h19M4 7h16M4 17h16"/></g></svg>
        vexalon.example
      </li>
    </ul>
    <div class="band band-orange"></div>
    <div class="band band-blue"></div>
  </section>

  <section class="card card-back">
    <p class="back-name">VEXALON</p>
    <p class="tagline">developer of custom applications</p>
    <p class="services"><span class="services-dot"></span>Bitcoin education &amp; payment integration</p>
  </section>
</body>
</html>
```